K Forgeworks Design and Analytics
Tech Consulting Company
K Forgeworks Design and Analytics - Information Technology
Creative Brief
Simple
Marcus Pellham
President/CEO
748 South Quillon Ave Baltimore, MD 21287
m.pellham@kfda-mail.com
Just the Logo on the back

```html
<!DOCTYPE html>
<html lang="en">
<head>
<meta charset="utf-8">
<title>K Forgeworks Design and Analytics – Stationery</title>
<link href="https://fonts.googleapis.com/css2?family=Roboto:wght@300;400;700&display=swap" rel="stylesheet">
<style>
  :root {
    --backdrop: #8b8b8b;
    --ink: #141414;
    --paper: #ffffff;
    --paper-shade: #ececec;
    --muted: #777777;
    --rule: #bdbdbd;
  }
  * { box-sizing: border-box; margin: 0; padding: 0; }
  html, body { width: 1200px; height: 480px; overflow: hidden; }
  body {
    background: var(--backdrop);
    font-family: "Roboto", Arial, sans-serif;
    color: var(--ink);
    position: relative;
  }
  .piece { position: absolute; background: var(--paper); box-shadow: 0 2px 6px rgba(0,0,0,.35); overflow: hidden; }
  .piece.dark { background: var(--ink); color: var(--paper); }
  .brand { font-weight: 700; letter-spacing: 2px; line-height: 1; }
  .dark .brand { color: var(--paper); }
  .tiny { font-size: 4px; line-height: 1.4; color: var(--muted); }
  .dark .tiny { color: #bbbbbb; }
  .band { position: absolute; left: 0; right: 0; background: var(--ink); }

  /* business cards */
  .card { left: 8px; width: 148px; height: 70px; }
  .card .brand { position: absolute; font-size: 16px; }
  .card-front-1 { top: 34px; }
  .card-front-1 .brand { left: 12px; top: 26px; }
  .card-back-1 { top: 110px; }
  .card-back-1 .brand { right: 10px; top: 10px; font-size: 11px; }
  .card-back-1 .details { position: absolute; left: 10px; bottom: 8px; }
  .card-back-1 .details .name { font-size: 6px; font-weight: 700; color: var(--ink); }
  .card-front-2 { top: 186px; }
  .card-front-2 .brand { left: 12px; top: 26px; }
  .card-back-2 { top: 262px; height: 64px; }
  .card-back-2 .brand { left: 12px; top: 10px; font-size: 10px; }
  .card-back-2 .web { position: absolute; right: 10px; bottom: 10px; font-size: 5px; color: #cccccc; }

  /* cd */
  .disc {
    position: absolute; left: 34px; top: 352px; width: 118px; height: 118px; border-radius: 50%;
    background: radial-gradient(circle, var(--backdrop) 0 9px, #d8d8d8 10px 17px, var(--paper) 18px);
    box-shadow: 0 2px 6px rgba(0,0,0,.35);
  }
  .disc .brand { position: absolute; left: 70px; top: 52px; font-size: 9px; }

  /* letterhead */
  .letterhead { left: 166px; top: 36px; width: 234px; height: 330px; padding: 20px 18px; }
  .letterhead .brand { font-size: 15px; margin-bottom: 20px; }
  .letterhead .recipient { margin-bottom: 10px; }
  .letterhead .body p { margin-bottom: 6px; }
  .letterhead .signature { font-size: 10px; font-style: italic; color: var(--ink); margin-top: 10px; }
  .letterhead .footer { position: absolute; left: 0; right: 0; bottom: 0; height: 16px; background: var(--ink); color: var(--paper); font-size: 5px; padding: 5px 18px; }

  /* fax */
  .fax { left: 396px; top: 222px; width: 124px; height: 170px; padding: 14px 12px; }
  .fax h2 { font-size: 12px; font-weight: 700; letter-spacing: 1px; margin-bottom: 10px; }
  .fax .field { border-bottom: 1px solid var(--rule); font-size: 5px; color: var(--muted); padding: 3px 0; }

  /* small envelopes */
  .dl-envelope { left: 168px; top: 400px; width: 160px; height: 70px; }
  .dl-envelope .brand { position: absolute; left: 12px; top: 10px; font-size: 10px; }
  .dl-envelope .band { bottom: 0; height: 10px; }
  .dl-envelope .web { position: absolute; left: 12px; bottom: 14px; font-size: 5px; color: var(--muted); }

  .slip { left: 418px; top: 36px; width: 144px; height: 72px; }
  .slip .brand { position: absolute; left: 12px; top: 12px; font-size: 10px; }
  .slip .band { bottom: 0; height: 8px; }

  .envelope { top: 58px; width: 150px; height: 132px; }
  .envelope .brand { position: absolute; left: 12px; top: 12px; font-size: 10px; }
  .envelope .flap { position: absolute; inset: 0; }
  .envelope-open { left: 570px; }
  .envelope-back { left: 724px; top: 60px; width: 150px; height: 70px; }
  .compliments { left: 724px; top: 186px; width: 150px; height: 74px; }
  .compliments .brand { position: absolute; left: 12px; top: 12px; font-size: 10px; }
  .compliments .label { position: absolute; right: 14px; top: 32px; font-size: 9px; font-style: italic; }
  .compliments .band { bottom: 0; height: 8px; }

  /* presentation slides */
  .slide { width: 116px; height: 96px; padding: 10px 8px; }
  .slide .title { font-size: 7px; font-weight: 700; }
  .slide .sub { font-size: 4px; color: var(--muted); margin-top: 2px; }
  .slide .brand { position: absolute; right: 8px; bottom: 8px; font-size: 7px; }
  .slide svg { position: absolute; }
  .slide-cover { left: 520px; top: 250px; width: 116px; height: 100px; }
  .slide-cover .title { margin-top: 26px; font-size: 9px; }
  .slide-bars { left: 640px; top: 216px; }
  .slide-pie { left: 520px; top: 356px; }
  .slide-bars-2 { left: 640px; top: 316px; }
  .slide-thanks { left: 760px; top: 300px; width: 118px; height: 108px; padding: 14px 10px; }
  .slide-thanks .title { margin-top: 34px; font-size: 8px; color: var(--paper); }
  .slide-thanks .sub { color: #bbbbbb; }

  /* folders */
  .folder-dark { left: 958px; top: 24px; width: 236px; height: 180px; }
  .folder-dark .half { position: absolute; top: 0; bottom: 0; width: 50%; }
  .folder-dark .half + .half { left: 50%; border-left: 1px solid #333333; }
  .folder-dark .brand { position: absolute; right: 14px; top: 14px; font-size: 14px; }
  .folder-dark .web { position: absolute; left: 12px; bottom: 12px; font-size: 5px; color: #bbbbbb; }

  .folder-light { left: 958px; top: 252px; width: 236px; height: 164px; }
  .folder-light svg { position: absolute; inset: 0; }
  .folder-light .brand { position: absolute; right: 14px; top: 12px; font-size: 12px; }
</style>
</head>
<body>

  <!-- business cards -->
  <div class="piece card card-front-1"><span class="brand">KFDA</span></div>
  <div class="piece card card-back-1">
    <span class="brand">KFDA</span>
    <div class="details tiny">
      <div class="name">Marcus Pellham</div>
      <div>President/CEO</div>
      <div>748 South Quillon Ave Baltimore, MD 21287</div>
      <div>m.pellham@kfda-mail.com</div>
    </div>
  </div>
  <div class="piece dark card card-front-2"><span class="brand">KFDA</span></div>
  <div class="piece dark card card-back-2">
    <span class="brand">KFDA</span>
    <span class="web">kfda-mail.com</span>
  </div>

  <!-- disc -->
  <div class="disc"><span class="brand">KFDA</span></div>

  <!-- letterhead -->
  <div class="piece letterhead">
    <div class="brand">KFDA</div>
    <div class="recipient tiny">
      <div>Client Name</div><div>Company Name</div><div>Street Address</div>
    </div>
    <div class="body tiny">
      <p>Dear Client,</p>
      <p>We appreciate your interest in our consulting services and look forward to working with you on your next project.</p>
      <p>Please review the enclosed proposal and contact us with any questions.</p>
      <p>Sincerely,</p>
    </div>
    <div class="signature">Marcus Pellham</div>
    <div class="tiny">President/CEO</div>
    <div class="footer">748 South Quillon Ave Baltimore, MD 21287 · kfda-mail.com</div>
  </div>

  <!-- fax -->
  <div class="piece fax">
    <h2>FAX</h2>
    <div class="field">To:</div>
    <div class="field">From:</div>
    <div class="field">Date:</div>
    <div class="field">Pages:</div>
  </div>

  <!-- envelopes -->
  <div class="piece dl-envelope">
    <span class="brand">KFDA</span>
    <span class="web">kfda-mail.com</span>
    <div class="band"></div>
  </div>
  <div class="piece slip"><span class="brand">KFDA</span><div class="band"></div></div>

  <div class="piece envelope envelope-open">
    <svg class="flap" viewBox="0 0 150 132" preserveAspectRatio="none">
      <polygon points="0,0 150,0 75,60" fill="var(--paper-shade)" stroke="var(--rule)" stroke-width="0.6"/>
      <line x1="0" y1="132" x2="60" y2="72" stroke="var(--rule)" stroke-width="0.6"/>
      <line x1="150" y1="132" x2="90" y2="72" stroke="var(--rule)" stroke-width="0.6"/>
    </svg>
  </div>
  <div class="piece dark envelope envelope-back">
    <svg class="flap" viewBox="0 0 150 70" preserveAspectRatio="none">
      <polygon points="0,0 150,0 75,40" fill="#2a2a2a"/>
    </svg>
  </div>
  <div class="piece compliments">
    <span class="brand">KFDA</span>
    <span class="label">With Compliments</span>
    <div class="band"></div>
  </div>

  <!-- presentation -->
  <div class="piece slide slide-cover">
    <div class="title">PRESENTATION NAME</div>
    <div class="sub">Presentation Title</div>
    <span class="brand">KFDA</span>
  </div>
  <div class="piece slide slide-bars">
    <div class="title">PRESENTATION HEADLINE</div>
    <svg viewBox="0 0 60 40" width="60" height="40" style="right:10px;top:30px">
      <rect x="0" y="2" width="50" height="5" fill="var(--ink)"/>
      <rect x="0" y="12" width="38" height="5" fill="#555"/>
      <rect x="0" y="22" width="44" height="5" fill="var(--ink)"/>
      <rect x="0" y="32" width="26" height="5" fill="#999"/>
    </svg>
    <span class="brand">KFDA</span>
  </div>
  <div class="piece slide slide-pie">
    <div class="title">PRESENTATION HEADLINE</div>
    <svg viewBox="0 0 40 40" width="44" height="44" style="right:14px;top:26px">
      <circle cx="20" cy="20" r="18" fill="#9a9a9a"/>
      <path d="M20 20 L20 2 A18 18 0 0 1 36 28 Z" fill="var(--ink)"/>
      <path d="M20 20 L36 28 A18 18 0 0 1 10 35 Z" fill="#555"/>
    </svg>
    <span class="brand">KFDA</span>
  </div>
  <div class="piece slide slide-bars-2">
    <div class="title">PRESENTATION HEADLINE</div>
    <svg viewBox="0 0 60 40" width="60" height="40" style="left:10px;top:30px">
      <rect x="2" y="20" width="8" height="20" fill="var(--ink)"/>
      <rect x="16" y="10" width="8" height="30" fill="#555"/>
      <rect x="30" y="24" width="8" height="16" fill="var(--ink)"/>
      <rect x="44" y="4" width="8" height="36" fill="#999"/>
    </svg>
    <span class="brand">KFDA</span>
  </div>
  <div class="piece dark slide slide-thanks">
    <div class="title">THANK YOU SO MUCH</div>
    <div class="sub">for your attention</div>
    <span class="brand">KFDA</span>
  </div>

  <!-- folders -->
  <div class="piece dark folder-dark">
    <div class="half"><span class="web">kfda-mail.com</span></div>
    <div class="half"><span class="brand">KFDA</span></div>
  </div>
  <div class="piece folder-light">
    <svg viewBox="0 0 236 164" preserveAspectRatio="none">
      <polygon points="0,164 0,70 118,164" fill="var(--ink)"/>
      <polygon points="236,164 236,70 118,164" fill="var(--ink)"/>
    </svg>
    <span class="brand">KFDA</span>
  </div>

</body>
</html>
```